Granite Ridge Response Business Card

Side 1: Granite Ridge Response Logo (logo without Maltese cross) with industrial rope rescue related theme. Our company services - TRAINING - Fire Training, Confined Space Rescue Training, Rope Rescue training, Hazmat Training, Incident Command, EMS, Pump Operations Training. Website - graniteridgeresponse.example.
Side 2: Granite Ridge Response Fire Department Logo (logo with Maltese cross) with Firefighter related theme. Company (division) services - FIELD SERVICES - Fire Department, Stand-by Rescue, Safety, EMS, Planning. "Supporting the Emergency Response Community Since 1967"

Add contact information wherever it makes since (Name, Email, Phone).
I would like it to represent the Granite Ridge Response Fire Department Logo as a division not as a separate entity without saying it, possibly by depicting it in the background of Side 2 instead of being a standalone picture like the logo on Side 1.

```html
<!DOCTYPE html>
<html lang="en">
<head>
<meta charset="utf-8">
<title>Granite Ridge Response Business Card</title>
<link href="https://fonts.googleapis.com/css2?family=Open+Sans:wght@400;600;700;800&display=swap" rel="stylesheet">
<style>
  :root {
    --backdrop: #dcdddf;
    --card: #1f1f22;
    --red: #e61e26;
    --white: #f4f4f4;
    --grey: #55565a;
    --rule: #bdbdbd;
  }
  * { box-sizing: border-box; margin: 0; padding: 0; }
  html, body { width: 1200px; height: 780px; overflow: hidden; }
  body {
    background: var(--backdrop);
    font-family: "Open Sans", Arial, sans-serif;
    color: var(--white);
    position: relative;
  }
  .card {
    position: absolute;
    top: 231px;
    width: 555px;
    height: 318px;
    background: var(--card);
    box-shadow: 0 6px 18px rgba(0,0,0,.25);
    overflow: hidden;
  }
  .card--contact { left: 30px; }
  .card--training { left: 615px; }

  /* Contact side */
  .brand-line {
    position: absolute; left: 34px; top: 26px;
    display: flex; align-items: center; gap: 10px;
  }
  .brand-dot { width: 18px; height: 18px; border-radius: 50%; background: var(--red); }
  .brand-name {
    font-weight: 800; font-size: 17px; letter-spacing: 1.5px;
    text-transform: uppercase; color: var(--white);
  }
  .person { position: absolute; left: 34px; top: 64px; }
  .person-name { font-weight: 800; font-size: 30px; line-height: 1; }
  .person-first { color: var(--red); }
  .person-last { color: var(--grey); }
  .person-title { font-size: 15px; margin-top: 5px; letter-spacing: .5px; }

  .services { position: absolute; left: 34px; top: 128px; width: 210px; }
  .services-heading {
    color: var(--red); font-weight: 700; font-size: 15px; line-height: 22px;
    text-transform: uppercase; margin-bottom: 3px;
  }
  .services-list { list-style: none; }
  .services-list li {
    font-size: 13.5px; line-height: 19px;
    display: flex; justify-content: flex-end; align-items: center; gap: 10px;
  }
  .services-list li::after {
    content: ""; width: 9px; height: 9px; border-radius: 50%; background: var(--red);
  }
  .divider {
    position: absolute; left: 262px; top: 134px; width: 1px; height: 112px;
    background: var(--rule); opacity: .7;
  }
  .contact { position: absolute; left: 284px; top: 96px; font-size: 13px; line-height: 20px; }
  .contact-address { margin-bottom: 4px; }
  .contact-row { display: flex; align-items: center; gap: 8px; }
  .contact-row svg { width: 13px; height: 13px; flex: none; }
  .tagline {
    position: absolute; left: 0; right: 0; bottom: 16px; height: 32px;
    background: var(--red); color: #fff;
    display: flex; align-items: center; justify-content: center;
    font-size: 14px; font-weight: 600; letter-spacing: .3px;
  }

  /* Training side */
  .training-brand {
    position: absolute; left: 0; right: 0; top: 70px;
    display: flex; flex-direction: column; align-items: center; gap: 14px;
  }
  .training-brand .brand-dot { width: 46px; height: 46px; }
  .training-brand .brand-name { font-size: 25px; letter-spacing: 2px; color: var(--red); }
  .training-heading {
    position: absolute; left: 26px; right: 26px; top: 182px;
    display: flex; align-items: center; gap: 10px;
    color: var(--red); font-weight: 700; font-size: 17px; letter-spacing: .5px;
  }
  .training-heading::before, .training-heading::after {
    content: ""; flex: 1; height: 2px; background: var(--white);
  }
  .training-list {
    position: absolute; left: 20px; right: 20px; top: 212px;
    list-style: none; display: flex; flex-wrap: wrap; justify-content: center;
    column-gap: 10px; row-gap: 2px;
  }
  .training-list li {
    font-size: 13px; line-height: 20px; display: flex; align-items: center; gap: 6px;
  }
  .training-list li::before {
    content: ""; width: 8px; height: 8px; border-radius: 50%; background: var(--red);
  }
  .training-list .row-break { flex-basis: 100%; height: 0; }
  .training-list .row-break::before { display: none; }
  .training-rule {
    position: absolute; left: 26px; right: 26px; height: 1px; background: var(--rule);
  }
  .training-rule--upper { top: 262px; }
  .training-rule--lower { top: 294px; opacity: .6; }
  .training-web {
    position: absolute; left: 0; right: 0; top: 266px; text-align: center;
    font-size: 14px; line-height: 22px; letter-spacing: .4px;
  }
</style>
</head>
<body>

<section class="card card--contact" aria-label="Contact side">
  <div class="brand-line">
    <span class="brand-dot"></span>
    <span class="brand-name">Granite Ridge Response</span>
  </div>

  <div class="person">
    <p class="person-name"><span class="person-first">Helena</span> <span class="person-last">Marsh</span></p>
    <p class="person-title">Director</p>
  </div>

  <div class="services">
    <p class="services-heading">Field Services</p>
    <ul class="services-list">
      <li>EMS</li>
      <li>Safety</li>
      <li>Planning</li>
      <li>Fire Department</li>
      <li>Stand-by Rescue</li>
    </ul>
  </div>

  <div class="divider"></div>

  <div class="contact">
    <p class="contact-address">418 Harbor Street<br>Lakeport, TX 77500</p>
    <p class="contact-row">
      <svg viewBox="0 0 24 24" aria-hidden="true"><path fill="#e61e26" d="M6.6 10.8a15 15 0 0 0 6.6 6.6l2.2-2.2c.3-.3.7-.4 1-.2 1.1.4 2.3.6 3.6.6.6 0 1 .4 1 1V20c0 .6-.4 1-1 1A17 17 0 0 1 3 4c0-.6.4-1 1-1h3.5c.6 0 1 .4 1 1 0 1.3.2 2.5.6 3.6.1.3 0 .7-.2 1z"/></svg>
      (555) 014-2290
    </p>
    <p class="contact-row">
      <svg viewBox="0 0 24 24" aria-hidden="true"><circle cx="12" cy="12" r="9" fill="none" stroke="#e61e26" stroke-width="2"/><path d="M3 12h18M12 3c3 3.5 3 14.5 0 18M12 3c-3 3.5-3 14.5 0 18" fill="none" stroke="#e61e26" stroke-width="1.6"/></svg>
      info@graniteridgeresponse.example
    </p>
    <p class="contact-row">
      <svg viewBox="0 0 24 24" aria-hidden="true"><rect x="3" y="5" width="18" height="14" rx="1.5" fill="none" stroke="#e61e26" stroke-width="2"/><path d="M3.5 6l8.5 7 8.5-7" fill="none" stroke="#e61e26" stroke-width="2"/></svg>
      www.graniteridgeresponse.example
    </p>
  </div>

  <p class="tagline">Supporting the Emergency Response Community Since 1967</p>
</section>

<section class="card card--training" aria-label="Training side">
  <div class="training-brand">
    <span class="brand-dot"></span>
    <span class="brand-name">Granite Ridge Response</span>
  </div>

  <p class="training-heading">TRAINING</p>

  <ul class="training-list">
    <li>Fire Training</li>
    <li>Confined Space Rescue Training</li>
    <li>Rope Rescue training</li>
    <li class="row-break" aria-hidden="true"></li>
    <li>Hazmat Training</li>
    <li>Incident Command</li>
    <li>EMS</li>
    <li>Pump Operations Training</li>
  </ul>

  <div class="training-rule training-rule--upper"></div>
  <p class="training-web">www.graniteridgeresponse.example</p>
  <div class="training-rule training-rule--lower"></div>
</section>

</body>
</html>
```